Financial Coaching biz needs modern service presentation menu

We need a PowerPoint presentation document with a modern, easy-to-read layout to share with potential clients.

I have a website under development that can be used as a reference www.brightledgerhub.com.

We'd like the doc to be simple to edit because services and verbiage will likely be modified periodically.

Two logo variations have been included.

Target Market(s)

Gen X, Gen Y, and Millienials

Industry/Entity Type

Financial Planning

Colors
85cae6
cadf82
ffffff
dddddd
cfcfcf
cee9f5

```html
<!DOCTYPE html>
<html lang="en">
<head>
<meta charset="utf-8">
<title>BrightLedger Hub – Pricing</title>
<link rel="stylesheet" href="https://fonts.googleapis.com/css2?family=Oswald:wght@300;500;700&family=Roboto+Mono:wght@700&display=swap">
<style>
  :root {
    --header-bg: #ebebeb;
    --page-bg: #d4d4d4;
    --brand-blue: #1d9ad6;
    --mascot-grey: #cfcfcf;
    --plan-blue: #1b63ad;
    --plan-navy: #1b4a7b;
    --plan-body: #666666;
    --pricing-head: #0a93d6;
    --pricing-body: #29a8e0;
    --white: #ffffff;
  }
  * { box-sizing: border-box; margin: 0; padding: 0; }
  html, body { width: 1200px; height: 848px; overflow: hidden; }
  body { background: var(--page-bg); position: relative; font-family: "Roboto Mono", monospace; font-weight: 700; color: var(--white); }

  .masthead { position: absolute; left: 0; top: 0; width: 1200px; height: 173px; background: var(--header-bg); overflow: hidden; }
  .brand { position: absolute; left: 70px; top: 40px; display: flex; align-items: center; gap: 22px; }
  .brand-mark { width: 86px; height: 86px; border-radius: 50%; background: var(--mascot-grey); }
  .brand-name { font-family: "Oswald", sans-serif; font-weight: 500; font-size: 50px; line-height: 52px; color: var(--brand-blue); letter-spacing: 1px; }
  .mascot-decor { position: absolute; left: 768px; top: 0; width: 416px; height: 173px; background: linear-gradient(180deg, #d9d9d9, #c9c9c9); border-radius: 0 0 40px 40px; }

  .plan { position: absolute; top: 196px; width: 270px; height: 632px; box-shadow: 0 6px 6px rgba(0,0,0,.25); }
  .plan-lifetime { left: 38px; --head: var(--plan-blue); }
  .plan-partner { left: 322px; --head: var(--plan-navy); }
  .plan-head { position: relative; height: 262px; background: var(--head); border-radius: 135px 135px 0 0 / 70px 70px 0 0; text-align: center; z-index: 2; }
  .plan-head::after { content: ""; position: absolute; left: 50%; bottom: -12px; transform: translateX(-50%); border-left: 12px solid transparent; border-right: 12px solid transparent; border-top: 12px solid var(--head); }
  .plan-head > * { position: absolute; left: 0; right: 0; }
  .plan-body { height: 370px; background: var(--plan-body); padding-top: 30px; text-align: center; }

  .plan-title { font-family: "Oswald", sans-serif; font-weight: 700; font-size: 27px; letter-spacing: 3px; line-height: 35px; }
  .rule { height: 1px; background: var(--white); left: 19px; right: 15px; }
  .big-price { font-family: "Oswald", sans-serif; font-weight: 500; font-size: 86px; line-height: 90px; margin-left: -20px; }
  .big-price sup, .mid-price sup, .full-price sup { font-size: 0.38em; vertical-align: top; position: relative; top: 0.3em; margin-right: 4px; font-weight: 500; }
  .mid-price { font-family: "Oswald", sans-serif; font-weight: 500; font-size: 56px; line-height: 60px; }
  .mid-price small { font-family: Georgia, serif; font-weight: 400; font-size: 16px; }
  .full-price { font-family: "Oswald", sans-serif; font-weight: 500; font-size: 56px; line-height: 60px; white-space: nowrap; }
  .full-price span { font-size: 30px; font-weight: 500; letter-spacing: 0; }
  .feature { font-size: 17px; line-height: 24.5px; margin: 0 auto 8px; width: 256px; }

  .pricing { position: absolute; left: 640px; top: 266px; width: 560px; height: 526px; background: var(--pricing-body); border-radius: 36px 0 0 36px; overflow: hidden; text-align: center; font-size: 15.5px; line-height: 24.5px; }
  .pricing-head { height: 86px; background: var(--pricing-head); font-family: "Oswald", sans-serif; font-weight: 500; font-size: 52px; line-height: 92px; }
  .pricing-body { padding: 20px 10px 0; }
  .gap-sm { height: 24px; }
  .gap-lg { height: 48px; }
</style>
</head>
<body>
  <header class="masthead">
    <div class="brand">
      <div class="brand-mark"></div>
      <div class="brand-name">BRIGHTLEDGER<br>HUB</div>
    </div>
    <div class="mascot-decor" role="img" aria-label="Large faint brand mascot decoration"></div>
  </header>

  <section class="plan plan-lifetime">
    <div class="plan-head">
      <h2 class="plan-title" style="top:53px">LIFETIME<br>MEMBERSHIP FEE</h2>
      <div class="rule" style="top:132px"></div>
      <p class="big-price" style="top:136px"><sup>$</sup>100</p>
    </div>
    <div class="plan-body">
      <p class="feature">Unlimited Access to Purchase Individual Services</p>
      <p class="feature">Free Access to One VIP Seminar per Year</p>
      <p class="feature">Free Access to One Money Event per Year</p>
    </div>
  </section>

  <section class="plan plan-partner">
    <div class="plan-head">
      <h2 class="plan-title" style="top:47px;font-size:24px">FULL PARTNERSHIP</h2>
      <p class="mid-price" style="top:80px"><sup>$</sup>75<small>/month</small></p>
      <div class="rule" style="top:150px;left:19px;right:19px"></div>
      <h3 class="plan-title" style="top:160px;font-size:24px">PAY IN FULL</h3>
      <p class="full-price" style="top:188px"><sup>$</sup>690<span>-23%DISC</span></p>
    </div>
    <div class="plan-body">
      <p class="feature">Monetary Action Plan with Unlimited Updates</p>
      <p class="feature">Personalized Budgeting Service</p>
      <p class="feature">BrightLedger's Exclusive Credit Plan Service</p>
      <p class="feature">Asset Advocacy for any major purchase</p>
      <p class="feature">Tax Preparation with Free Amendments</p>
    </div>
  </section>

  <section class="pricing">
    <h2 class="pricing-head">PRICING</h2>
    <div class="pricing-body">
      <p>ALL Special Benefits including:<br>Savings Builder with Annual Cash Bonus**<br>In-person Budget Coach Service<br>Coupon Finder<br>VIP Seminar Access</p>
      <div class="gap-sm"></div>
      <p>No-Hassle, Free Cancellation at any time</p>
      <div class="gap-lg"></div>
      <p>$180/2-month access<br>Choose one Individual Service Option<br>Choose one Special Benefit (excludes Savings Builder)</p>
      <div class="gap-sm"></div>
      <p>*Total balance must be paid in full within first 60 days of service<br>**Savings Builder only available with Full Partnership</p>
    </div>
  </section>
</body>
</html>
```